Poster Design Project - Wine/Tapas/Jazz Night

Design of poster & menu for Wine/Tapas/Jazz night based on previous poster & menu for a previous event

Details to Edit:
Date: Saturday 8th June
Band: Gordon Brae Jazz Trio
Wines: Kelverdale replaced by Tall Crow Wines (Graphics to follow)
Updates

Band Photo has just been added

Target Market(s)

50+ age group

Industry/Entity Type

Event

Requirements
Must have
• Must be similar in style to previous Poster & Menu

```html
<!DOCTYPE html>
<html lang="en">
<head>
<meta charset="utf-8">
<title>Wine/Tapas/Jazz</title>
<link href="https://fonts.googleapis.com/css2?family=Cabin:wght@400;500&family=Arimo:wght@700&display=swap" rel="stylesheet">
<style>
  :root {
    --paper: #efece4;
    --header-band: #d5d3ea;
    --header-column: #dac8f1;
    --title: #5b515f;
    --photo-sky: #6f8596;
    --photo-land: #5b5a36;
    --photo-case: #5a3426;
    --night-band: #22062e;
    --jazz-light: #c9a5e4;
    --jazz-dark: #6d3b8e;
    --body-column: #f2d9f3;
    --item-text: #8c55a3;
    --tick: #a57bbd;
    --phone: #7e4c99;
    --guest-box: rgba(245, 245, 250, 0.72);
    --guest-text: #2c2530;
  }
  html, body {
    margin: 0;
    padding: 0;
    overflow: hidden;
  }
  body {
    width: 849px;
    height: 1200px;
    background: var(--paper);
    font-family: "Cabin", "Gill Sans", sans-serif;
  }
  .poster {
    position: relative;
    width: 849px;
    height: 1200px;
    overflow: hidden;
    background: var(--paper);
  }
  .header-band {
    position: absolute;
    left: 0; top: 0;
    width: 849px; height: 203px;
    background: var(--header-band);
  }
  .header-column {
    position: absolute;
    left: 92px; top: 0;
    width: 665px; height: 203px;
    background: var(--header-column);
  }
  .event-title {
    position: absolute;
    left: 165px; top: 70px;
    margin: 0;
    font-size: 62px;
    font-weight: 500;
    letter-spacing: -1px;
    color: var(--title);
    text-shadow: 3px 3px 2px rgba(60, 50, 70, 0.45);
    line-height: 1;
  }
  .hero-photo {
    position: absolute;
    left: 0; top: 203px;
    width: 849px; height: 244px;
    background:
      linear-gradient(90deg, var(--photo-land) 0%, #6b4a34 22%, var(--photo-case) 45%, #4a4c48 62%, var(--photo-sky) 80%, #3f5058 100%);
  }
  .guest-box {
    position: absolute;
    left: 406px; top: 205px;
    width: 434px; height: 119px;
    background: var(--guest-box);
    border-radius: 4px;
    text-align: center;
    color: var(--guest-text);
    font-size: 24px;
    line-height: 31px;
    padding-top: 3px;
    box-sizing: border-box;
    letter-spacing: -0.5px;
  }
  .night-band {
    position: absolute;
    left: 0; top: 447px;
    width: 849px; height: 81px;
    background: var(--night-band);
  }
  .jazz-mark {
    position: absolute;
    left: 512px; top: 388px;
  }
  .body-column {
    position: absolute;
    left: 92px; top: 528px;
    width: 665px; height: 672px;
    background: var(--body-column);
  }
  .details {
    position: absolute;
    left: 143px; top: 588px;
    width: 600px;
    margin: 0; padding: 0;
    list-style: none;
  }
  .detail {
    position: absolute;
    left: 0;
    width: 600px;
    color: var(--item-text);
    font-size: 31px;
    line-height: 37px;
    letter-spacing: -0.3px;
  }
  .detail-text { display: block; width: 480px; }
  .detail .tick {
    position: absolute;
    left: 505px;
  }
  .detail-band { top: 0; }
  .detail-band .tick { top: -2px; }
  .detail-wines { top: 130px; }
  .detail-wines .tick { top: -5px; }
  .detail-date { top: 274px; }
  .detail-date .tick { top: -12px; }
  .booking-phone {
    position: absolute;
    left: 92px; top: 1027px;
    width: 665px;
    text-align: center;
    font-family: "Arimo", Arial, sans-serif;
    font-weight: 700;
    font-size: 72px;
    color: var(--phone);
    margin: 0;
    line-height: 1;
  }
</style>
</head>
<body>
<main class="poster">
  <div class="header-band"></div>
  <div class="header-column"></div>
  <h1 class="event-title">Wine/Tapas/Jazz</h1>

  <div class="hero-photo" role="img" aria-label="Saxophone and keyboard resting on a leather case on a coastal clifftop, with a singer by the sea"></div>

  <div class="guest-box">
    With special guests:<br>
    Martin Hale and<br>
    Ross Delaney
  </div>

  <div class="night-band"></div>

  <svg class="jazz-mark" width="200" height="140" viewBox="0 0 200 140" aria-label="Jazz">
    <defs>
      <linearGradient id="jazzFill" x1="0" y1="0" x2="0" y2="1">
        <stop offset="0" stop-color="var(--jazz-light)"/>
        <stop offset="1" stop-color="var(--jazz-dark)"/>
      </linearGradient>
      <linearGradient id="jazzFade" x1="0" y1="0" x2="0" y2="1">
        <stop offset="0" stop-color="#8e63ad" stop-opacity="0.55"/>
        <stop offset="1" stop-color="#8e63ad" stop-opacity="0"/>
      </linearGradient>
    </defs>
    <text x="4" y="92" font-family="Cabin, sans-serif" font-size="92" fill="url(#jazzFill)" stroke="#f1e4fa" stroke-width="1">Jazz</text>
    <text x="4" y="-96" font-family="Cabin, sans-serif" font-size="92" fill="url(#jazzFade)" transform="scale(1,-1)">Jazz</text>
  </svg>

  <div class="body-column"></div>

  <ul class="details">
    <li class="detail detail-band">
      <span class="detail-text">Gordon Brae Jazz Trio</span>
      <svg class="tick" width="80" height="70" viewBox="0 0 80 70" aria-hidden="true">
        <path d="M4 38 Q12 36 20 60 Q36 22 76 3 Q42 28 22 68 Q14 48 4 38 Z" fill="var(--tick)"/>
      </svg>
    </li>
    <li class="detail detail-wines">
      <span class="detail-text">Kelverdale Replaced by Tall Crow Wines</span>
      <svg class="tick" width="80" height="70" viewBox="0 0 80 70" aria-hidden="true">
        <path d="M4 38 Q12 36 20 60 Q36 22 76 3 Q42 28 22 68 Q14 48 4 38 Z" fill="var(--tick)"/>
      </svg>
    </li>
    <li class="detail detail-date">
      <span class="detail-text">Saturday, June 8, 2013</span>
      <svg class="tick" width="80" height="70" viewBox="0 0 80 70" aria-hidden="true">
        <path d="M4 38 Q12 36 20 60 Q36 22 76 3 Q42 28 22 68 Q14 48 4 38 Z" fill="var(--tick)"/>
      </svg>
    </li>
  </ul>

  <p class="booking-phone">1800 462 462</p>
</main>
</body>
</html>
```